Business Card for Lorena Whitfield

Name: Lorena Whitfield
Title: Realtor
Email: Lorena@LorenaWhitfieldRE.com
Phone: 480-555-0137

On the front of the business card, I would like the photo, the contact information and the Lorena Whitfield Logo. The backside is required to have the Broker logo and the required logos. Please use the colors from the logo design. Our company has a classy, professional look.

```html
<!DOCTYPE html>
<html lang="en">
<head>
<meta charset="utf-8">
<title>Lorena Whitfield — Business Card</title>
<link rel="stylesheet" href="https://fonts.googleapis.com/css2?family=Cinzel:wght@400&family=Libre+Baskerville:wght@700&family=Arimo:wght@400&display=swap">
<style>
  :root {
    --bg: #e9e8e6;
    --paper: #f7f7f6;
    --brand-red: #b8172f;
    --ink: #3d3d3f;
    --charcoal: #29292b;
    --charcoal-soft: #3a3a3d;
    --silver: #e4e4e4;
    --emboss: #48484b;
    --photo-light: #c9c9c9;
    --photo-dark: #2b2b2b;
  }
  * { margin: 0; padding: 0; box-sizing: border-box; }
  html, body { width: 1200px; height: 801px; overflow: hidden; }
  body {
    background: var(--bg);
    position: relative;
    font-family: "Arimo", Arial, sans-serif;
  }
  .card {
    position: absolute;
    top: 252px;
    width: 530px;
    height: 303px;
    border-radius: 4px;
    box-shadow: 0 10px 28px rgba(0,0,0,0.18);
    overflow: hidden;
  }
  /* Front */
  .card-front { left: 45px; background: var(--paper); }
  .portrait {
    position: absolute;
    right: 0; top: 0;
    width: 230px; height: 303px;
    background: linear-gradient(180deg, var(--photo-light) 0%, #8f8f8f 45%, var(--photo-dark) 70%, #1e1e1e 100%);
    clip-path: polygon(22% 8%, 60% 4%, 82% 22%, 100% 30%, 100% 100%, 10% 100%, 14% 62%, 18% 40%);
  }
  .brand {
    position: absolute;
    left: 34px; top: 34px;
    display: flex; align-items: center; gap: 12px;
  }
  .brand-mark {
    width: 40px; height: 40px;
    border: 2px solid var(--brand-red);
  }
  .brand-name {
    font-family: "Cinzel", Georgia, serif;
    color: var(--brand-red);
    font-size: 23px;
    letter-spacing: 1px;
    line-height: 1;
  }
  .brand-tag {
    display: block;
    font-size: 11px;
    letter-spacing: 1.5px;
    margin-top: 4px;
    text-align: right;
  }
  .agent { position: absolute; left: 46px; top: 150px; }
  .agent-name {
    font-family: "Libre Baskerville", Georgia, serif;
    font-weight: 700;
    color: var(--brand-red);
    font-size: 22px;
  }
  .agent-title { color: var(--ink); font-size: 16px; margin-top: 3px; }
  .contact { position: absolute; left: 46px; top: 222px; list-style: none; }
  .contact li {
    display: flex; align-items: center; gap: 9px;
    color: var(--ink); font-size: 16px; margin-bottom: 6px;
  }
  .contact svg { width: 13px; height: 13px; fill: var(--brand-red); flex: none; }
  .edge-tab {
    position: absolute; left: 0; bottom: 42px;
    width: 20px; height: 30px;
    background: var(--brand-red);
    border-radius: 0 3px 3px 0;
  }
  /* Back */
  .card-back {
    left: 625px;
    background: linear-gradient(160deg, var(--charcoal-soft), var(--charcoal) 60%);
  }
  .back-brand {
    position: absolute; left: 50%; top: 62px;
    transform: translateX(-50%);
    display: flex; align-items: center; gap: 14px;
  }
  .back-brand .brand-mark { width: 46px; height: 46px; border-color: var(--emboss); }
  .back-brand .brand-name { color: var(--emboss); font-size: 27px; }
  .affiliations {
    position: absolute; left: 0; right: 0; bottom: 44px;
    display: flex; justify-content: space-around; align-items: center;
    padding: 0 30px;
  }
  .broker {
    font-family: "Cinzel", Georgia, serif;
    color: var(--silver);
    text-align: center;
    font-size: 12px; letter-spacing: 1px; line-height: 1.3;
  }
  .broker-tag { display: block; font-size: 7px; letter-spacing: 1.5px; }
  .badge-housing {
    width: 64px; height: 58px;
    border: 4px solid var(--silver);
    border-radius: 2px;
  }
  .badge-listing {
    width: 128px; height: 56px;
    border: 3px solid var(--silver);
  }
</style>
</head>
<body>
  <section class="card card-front">
    <div class="brand">
      <span class="brand-mark"></span>
      <span class="brand-name">LORENA WHITFIELD<span class="brand-tag">REAL ESTATE</span></span>
    </div>
    <div class="portrait" role="img" aria-label="Black and white portrait photo of the realtor"></div>
    <div class="agent">
      <p class="agent-name">Lorena Whitfield</p>
      <p class="agent-title">Realtor</p>
    </div>
    <ul class="contact">
      <li>
        <svg viewBox="0 0 24 24" aria-hidden="true"><path d="M6.6 10.8a15 15 0 0 0 6.6 6.6l2.2-2.2a1 1 0 0 1 1-.25 11.4 11.4 0 0 0 3.6.57 1 1 0 0 1 1 1V20a1 1 0 0 1-1 1A17 17 0 0 1 3 4a1 1 0 0 1 1-1h3.5a1 1 0 0 1 1 1c0 1.25.2 2.45.57 3.57a1 1 0 0 1-.25 1z"/></svg>
        480-555-0137
      </li>
      <li>
        <svg viewBox="0 0 24 24" aria-hidden="true"><path d="M2 5h20v14H2z M2 5l10 8 10-8" stroke="#f7f7f6" stroke-width="1.5"/></svg>
        Lorena@LorenaWhitfieldRE.com
      </li>
    </ul>
    <span class="edge-tab"></span>
  </section>

  <section class="card card-back">
    <div class="back-brand">
      <span class="brand-mark"></span>
      <span class="brand-name">LORENA WHITFIELD<span class="brand-tag">REAL ESTATE</span></span>
    </div>
    <div class="affiliations">
      <p class="broker">HAROLD PIERCE<span class="broker-tag">REAL ESTATE</span></p>
      <span class="badge-housing" role="img" aria-label="Fair housing badge"></span>
      <span class="badge-listing" role="img" aria-label="Professional association and listing service badge"></span>
    </div>
  </section>
</body>
</html>
```